QTR business cards

I need a Business card design for my self. I am behavior analyst owner of a new company based in Miami. We offer Applied Behavior Analysis (ABA) services to individuals with developmental disabilities.

Business

```html
<!DOCTYPE html>
<html lang="en">
<head>
<meta charset="utf-8">
<title>QTR Business Cards</title>
<link rel="stylesheet" href="https://fonts.googleapis.com/css2?family=Source+Sans+3:wght@400;600;700&display=swap">
<style>
  :root {
    --green: #4e9a2e;
    --navy: #173f78;
    --paper: #ffffff;
    --backdrop: #3d3d3d;
  }
  * { margin: 0; padding: 0; box-sizing: border-box; }
  html, body {
    width: 1029px; height: 1200px; overflow: hidden;
    background: var(--backdrop);
    font-family: "Source Sans 3", "Myriad Pro", sans-serif;
  }
  .card {
    position: absolute; left: 84px;
    width: 860px; height: 491px;
    background: var(--paper);
    overflow: hidden;
  }
  .card--front { top: 80px; }
  .card--back { top: 620px; }
  .corner { position: absolute; width: 72px; height: 42px; }
  .corner--tl { top: 0; left: 0; }
  .corner--br { bottom: 0; right: 0; }
  .holder { position: absolute; left: 36px; top: 96px; color: var(--green); }
  .holder__name { font-size: 42px; font-weight: 400; line-height: 1; letter-spacing: 0.2px; }
  .holder__title { font-size: 16.5px; font-weight: 600; margin-top: 6px; }
  .contact {
    position: absolute; left: 0; width: 318px; height: 44px;
    background: var(--green); color: var(--paper);
    border-radius: 0 22px 22px 0;
    font-size: 22px; line-height: 44px; padding-left: 31px;
  }
  .contact--phone { top: 274px; }
  .contact--email { top: 334px; }
  .services {
    position: absolute; left: 32px; top: 408px;
    display: grid; grid-template-columns: 318px auto; row-gap: 4px;
    list-style: none; color: var(--navy); font-size: 22.5px;
  }
  .services li { display: flex; align-items: center; gap: 9px; line-height: 28px; }
  .services li::before {
    content: ""; width: 8px; height: 8px; background: var(--navy);
    transform: rotate(45deg); flex: none;
  }
  .brand {
    position: absolute; display: flex; align-items: center;
    color: var(--navy); font-weight: 700;
  }
  .brand__dot { border-radius: 50%; background: var(--green); flex: none; }
  .card--front .brand { right: 48px; top: 210px; font-size: 58px; gap: 12px; }
  .card--front .brand__dot { width: 26px; height: 26px; }
  .card--back .brand {
    left: 0; right: 0; top: 0; bottom: 0;
    justify-content: center; font-size: 128px; gap: 26px;
  }
  .card--back .brand__dot { width: 52px; height: 52px; }
</style>
</head>
<body>
  <section class="card card--front">
    <svg class="corner corner--tl" viewBox="0 0 72 42"><polygon points="0,0 72,0 0,42" fill="var(--green)"/></svg>
    <div class="holder">
      <h1 class="holder__name">Marisol Ortega, B.A.</h1>
      <p class="holder__title">Board Certified Asst. Behavior Analyst (BCABA)</p>
    </div>
    <div class="contact contact--phone">Phone: 786-555-0142</div>
    <div class="contact contact--email">ortega.m.cba@mailbox.com</div>
    <ul class="services">
      <li>Applied Behavior Analysis</li>
      <li>Parent/Teacher Training</li>
      <li>Social Skills Training</li>
      <li>Tutoring</li>
    </ul>
    <div class="brand"><span class="brand__dot"></span>QTR</div>
    <svg class="corner corner--br" viewBox="0 0 72 42"><polygon points="72,0 72,42 0,42" fill="var(--green)"/></svg>
  </section>

  <section class="card card--back">
    <svg class="corner corner--tl" viewBox="0 0 72 42"><polygon points="0,0 72,0 0,42" fill="var(--green)"/></svg>
    <div class="brand"><span class="brand__dot"></span>QTR</div>
    <svg class="corner corner--br" viewBox="0 0 72 42"><polygon points="72,0 72,42 0,42" fill="var(--green)"/></svg>
  </section>
</body>
</html>
```